Redesign for luxury lifestyle PR agency

Copper Fern Heron is a luxury lifestyle public relations agency specialising in indigenous and regenerative travel. We are the elephant you want in the room. We represent interesting brands and people who would be described as changemakers in their respective fields. The winning design should be stylish, clean cut and earthy. It should communicate that Copper Fern Heron is professional and representative of the industries that it serves. The purpose of the website is to provide clear information to potential customers and media, improve the image and brand of the company, position the company as one of scale and increase sales conversions. Its aesthetic will be aspirational and image led in an editorial style. I would like to be able to easily edit the website once finished and be able to work with the designer on an ad hoc basis once the project is completed.

Please see below for some website I like the style of:

https://www.vantorelle-studio.com/

https://www.quillbrightglobal.com/

https://www.tessamorrowhome.co.uk/

Pages I would like to include are:

Home
Services
Clients
Testimonials
About Us
News

I'm also attaching a proposal that I really liked the style of and I would like this sort of aesthetic on the website too. My logo is also attached (it is likely that the colour palette might change with the website).

I'm open to inspiration on the colours - my immediate preference is greens and/or blues.

Here is the existing website that I built myself on Wix - https://www.copperfernheron.com/ (it looks so outdated and amateur now hence the need of a serious rebrand)

Target Market(s)

Luxury travel and lifestyle brands

Industry/Entity Type

Luxury travel and lifestyle

Number of Pages Required

1 page

Font styles to use
Serif
Other font styles liked:
• Open to suggestions

Requirements
Must have
• Beautiful imagery

```html
<!DOCTYPE html>
<html lang="en">
<head>
<meta charset="utf-8">
<title>Copper Fern Heron — Website Design</title>
<link rel="stylesheet" href="https://fonts.googleapis.com/css2?family=Libre+Caslon+Text:ital,wght@0,400;0,700;1,400&display=swap">
<style>
:root{
  --navy:#22185f;
  --ink:#2a2168;
  --cream:#faf3ec;
  --paper:#ffffff;
  --mist:#f4f3f3;
  --lilac:#6d6fa6;
  --sea:#3a86c8;
  --sky:#6aa6e0;
  --sand:#d9c7a6;
  --rule:#2a2168;
}
*{box-sizing:border-box;margin:0;padding:0}
html,body{width:852px;height:1200px;overflow:hidden;background:var(--paper)}
body{position:relative;font-family:"Libre Caslon Text",Georgia,serif;color:var(--ink)}
.abs{position:absolute}
.photo{position:absolute;display:block}
.rule{position:absolute;height:1px;background:var(--rule)}
.rule.light{background:#fff}
svg.icons{display:none}
.icon{width:14px;height:14px;stroke:#fff;fill:none;stroke-width:1}

/* desktop hero screen */
.desktop{left:210px;top:48px;width:415px;height:259px;background:var(--cream);overflow:hidden}
.service-title{font-weight:700;color:var(--ink)}
.services-band{position:absolute;background:var(--navy);display:flex;align-items:center;color:#fff}
.service-item{display:flex;flex-direction:column;gap:3px;font-size:5.4px;line-height:1.3;font-weight:700}

/* phone screen */
.phone{left:666px;top:147px;width:103px;height:220px;background:var(--cream);border-radius:10px;overflow:hidden;border:1px solid #e7dfd6}
.btn{position:absolute;border:1px solid var(--ink);border-radius:20px;color:var(--ink);font-weight:700;display:flex;align-items:center;justify-content:center}

/* left page */
.page-left{left:50px;top:375px;width:350px;height:806px;background:var(--cream)}
.section-heading{position:absolute;left:0;width:100%;text-align:center;font-size:11.5px;color:var(--ink)}
.testimonials{position:absolute;left:0;top:190px;width:350px;height:143px;background:linear-gradient(180deg,#7a7fb6,#6467a0 60%,#7478ad);color:#fff;text-align:center}
.who{position:absolute;left:0;top:333px;width:350px;height:212px}
.who-panel{position:absolute;left:114px;top:0;width:236px;height:212px;background:var(--navy);color:#fff}
.who p{font-size:4.3px;line-height:1.6;width:160px}
.news{position:absolute;left:0;top:545px;width:350px;height:210px;background:var(--mist)}
.news-card{position:absolute;top:38px;width:85px}
.news-card h4{font-size:4.4px;font-weight:700;margin:6px 0 3px;color:#111}
.news-card p{font-size:3.6px;line-height:1.55;color:#222}
.footer{position:absolute;left:0;top:755px;width:350px;height:51px;background:var(--navy);color:#fff}

/* right page */
.page-right{left:443px;top:395px;width:362px;height:805px;background:var(--cream);overflow:hidden}
.brand{position:absolute;left:0;width:100%;top:18px;display:flex;justify-content:center;align-items:center;gap:4px;font-size:7px;color:var(--sea);letter-spacing:.3px}
.brand .dot{width:6px;height:6px;border-radius:50%;background:var(--sea)}
.nav{position:absolute;top:50px;left:0;width:100%;display:flex;justify-content:center;gap:11px;font-size:5px;color:#111}
</style>
</head>
<body>

<svg class="icons" aria-hidden="true">
  <symbol id="i-plan" viewBox="0 0 16 16"><rect x="2" y="4" width="10" height="10"/><path d="M6 4V2h8v8h-2M5 11l3-3 2 2 3-4"/></symbol>
  <symbol id="i-media" viewBox="0 0 16 16"><circle cx="4.5" cy="4.5" r="3"/><circle cx="11.5" cy="4.5" r="3"/><circle cx="4.5" cy="11.5" r="3"/><circle cx="11.5" cy="11.5" r="3"/></symbol>
  <symbol id="i-rep" viewBox="0 0 16 16"><rect x="1.5" y="3" width="13" height="11"/><path d="M1.5 6h13M4 12l3-3 2 2 3-3"/></symbol>
  <symbol id="i-star" viewBox="0 0 16 16"><path d="M8 1.5l2 4.3 4.6.5-3.4 3.1 1 4.6L8 11.7 3.8 14l1-4.6L1.4 6.3 6 5.8z"/><circle cx="8" cy="8.3" r="1.6"/></symbol>
  <symbol id="i-idea" viewBox="0 0 16 16"><circle cx="8" cy="7" r="4.5"/><path d="M6 11.5v2.5h4v-2.5M8 1v1.5M2 7h1.5M12.5 7H14"/></symbol>
</svg>

<!-- Desktop hero: services -->
<section class="abs desktop" aria-label="Our Service, desktop view">
  <h2 class="abs service-title" style="left:24px;top:64px;font-size:13px">Our Service</h2>
  <div class="rule" style="left:24px;top:83px;width:16px"></div>
  <p class="abs" style="left:24px;top:89px;font-size:9px">Pure &amp; Simple</p>
  <p class="abs" style="left:24px;top:108px;width:160px;font-size:9.2px;line-height:1.45">No-nonsense approach to launching new brands to the UK market, offering a completely bespoke service to include</p>
  <div class="photo" role="img" aria-label="Photograph of a white resort hotel above a blue pool" style="left:242px;top:9px;width:150px;height:168px;border-radius:75px 75px 0 0;background:linear-gradient(180deg,#7fb3e4 0%,#cfe0ea 40%,#c9c1b3 62%,#3b7fbf 100%)"></div>
  <div class="services-band" style="left:-3px;top:178px;width:340px;height:81px;padding-left:27px;gap:22px">
    <div class="service-item"><svg class="icon"><use href="#i-plan"/></svg>Strategic<br>Planning</div>
    <div class="service-item"><svg class="icon"><use href="#i-media"/></svg>Consumer<br>Media Relations</div>
    <div class="service-item"><svg class="icon"><use href="#i-rep"/></svg>Reputation<br>Management</div>
    <div class="service-item"><svg class="icon"><use href="#i-star"/></svg>Influencer<br>Management</div>
    <div class="service-item"><svg class="icon"><use href="#i-idea"/></svg>Creative<br>Consultation</div>
  </div>
</section>

<!-- Mobile view -->
<section class="abs phone" aria-label="Mobile view">
  <div class="rule" style="left:44px;top:25px;width:16px"></div>
  <p class="abs" style="left:8px;top:33px;width:87px;text-align:center;font-size:5px;line-height:1.5">Copper Fern Heron is a boutique lifestyle PR and communications agency helping brands get their voices heard in the UK.</p>
  <div class="btn" style="left:28px;top:79px;width:47px;height:14px;font-size:5px">Get in touch</div>
  <h2 class="abs service-title" style="left:11px;top:141px;font-size:8px">Our Service</h2>
  <div class="rule" style="left:11px;top:152px;width:15px"></div>
  <p class="abs" style="left:14px;top:158px;font-size:5px">Pure &amp; Simple</p>
  <p class="abs" style="left:12px;top:171px;width:82px;font-size:5px;line-height:1.5">No-nonsense approach to launching new brands to the UK market, offering a completely bespoke service to include</p>
</section>

<!-- Left page: clients, testimonials, about, news -->
<main class="abs page-left">
  <h2 class="section-heading" style="top:20px">Past Clients</h2>
  <div class="rule" style="left:165px;top:38px;width:15px"></div>
  <div class="photo" role="img" aria-label="Client photo: Selvane &amp; Co" style="left:48px;top:62px;width:59px;height:42px;background:#5b4a3e"><span style="position:absolute;left:20px;top:33px;font-size:3.5px;color:#fff">Selvane &amp; Co</span></div>
  <div class="photo" role="img" aria-label="Client photo: restaurant terrace" style="left:114px;top:62px;width:59px;height:42px;background:linear-gradient(180deg,#c97a5a,#6b3b2c)"></div>
  <div class="photo" role="img" aria-label="Client photo: framed portrait" style="left:181px;top:62px;width:59px;height:42px;background:radial-gradient(circle,#8a7040 30%,#eae6e1 60%)"></div>
  <div class="photo" role="img" aria-label="Client photo: framed portrait" style="left:248px;top:62px;width:59px;height:42px;background:radial-gradient(circle,#8a7040 30%,#eae6e1 60%)"></div>
  <div class="photo" role="img" aria-label="Client photo: dinner table setting" style="left:48px;top:108px;width:59px;height:42px;background:linear-gradient(135deg,#4d5a6e,#c4c8cf)"></div>
  <div class="photo" role="img" aria-label="Client photo: car on a beach" style="left:114px;top:108px;width:59px;height:42px;background:linear-gradient(180deg,#3b74c4 55%,#d9bd86 55%)"></div>
  <div class="photo" role="img" aria-label="Client photo: pour-over coffee" style="left:181px;top:108px;width:59px;height:42px;background:linear-gradient(90deg,#6e5444,#e9e3dc,#6e5444)"></div>
  <div class="photo" role="img" aria-label="Client photo: pour-over coffee" style="left:248px;top:108px;width:59px;height:42px;background:linear-gradient(90deg,#6e5444,#e9e3dc,#6e5444)"></div>

  <section class="testimonials" role="img" aria-label="Testimonials over a photo of a seaside terrace">
    <h2 style="position:absolute;top:23px;width:100%;font-size:11.5px;font-weight:400">Testimonials</h2>
    <div class="rule light" style="left:167px;top:40px;width:15px"></div>
    <p style="position:absolute;top:50px;width:100%;font-size:4.2px;font-style:italic">Clara Whitcombe, Partner at Lindqvale</p>
    <p style="position:absolute;top:64px;left:82px;width:186px;font-size:8.4px;line-height:1.5">“I'm a testimonial. Click to edit me and add text that says something nice about you and your services.”</p>
    <p style="position:absolute;top:108px;width:100%;font-size:8px;letter-spacing:1px">•••</p>
  </section>

  <section class="who">
    <div class="who-panel">
      <h2 style="position:absolute;left:55px;top:30px;font-size:11px;font-weight:400">Who We Are</h2>
      <div class="rule light" style="left:55px;top:45px;width:15px"></div>
      <p style="position:absolute;left:55px;top:66px">Maren Ashdown founded Copper Fern Heron in 2016 after working for one of the most reputable luxury travel PR agencies in London, leading a team that launched some of the world's most iconic hotels, as well as spending time at a national newspaper. She understands what it is like to be on either side of the PR coin and what it takes to create a juicy story.</p>
      <p style="position:absolute;left:55px;top:127px">Copper Fern Heron works as an extension to your team providing a service that feels in-house. Maren prefers a direct approach and will always pick up the phone to sound out an idea and probably ask what you're planning for dinner too. The Copper Fern Heron clients are a carefully curated list and they feel like family.</p>
    </div>
    <div class="photo" role="img" aria-label="Black and white portrait of the founder" style="left:85px;top:61px;width:65px;height:97px;background:linear-gradient(180deg,#9a9a9a,#3d3d3d)"></div>
  </section>

  <section class="news">
    <h2 class="section-heading" style="top:18px">News</h2>
    <div class="rule" style="left:168px;top:36px;width:15px"></div>
    <article class="news-card" style="left:22px">
      <div role="img" aria-label="Blog photo: man relaxing on a terrace sofa" style="height:60px;background:linear-gradient(180deg,#c9d3cf,#e9e4dd 60%,#c08a5e)"></div>
      <h4>Managing your business made easy</h4>
      <p>Welcome to your blog post. Use this space to connect with your readers and potential customers in a way that's current and interesting...</p>
    </article>
    <article class="news-card" style="left:133px">
      <div role="img" aria-label="Blog photo: hands holding cocktails" style="height:60px;background:linear-gradient(135deg,#e8dcd8,#7a5a8e 45%,#3a2a24)"></div>
      <h4>Managing your business made easy</h4>
      <p>Welcome to your blog post. Use this space to connect with your readers and potential customers in a way that's current and interesting...</p>
    </article>
    <article class="news-card" style="left:242px">
      <div role="img" aria-label="Blog photo: resort pool with palms" style="height:60px;background:linear-gradient(180deg,#5f8b55,#dfe6e0 50%,#2aa3ad)"></div>
      <h4>Managing your business made easy</h4>
      <p>Welcome to your blog post. Use this space to connect with your readers and potential customers in a way that's current and interesting...</p>
    </article>
  </section>

  <footer class="footer">
    <p style="position:absolute;left:22px;top:19px;font-size:8.4px;line-height:1.45">The best relationships<br>start at hello....</p>
    <p style="position:absolute;left:170px;top:27px;font-size:4.6px">maren@copperfernheron.com</p>
    <p style="position:absolute;left:282px;top:28px;font-size:4.6px">+44 (0) 7700 900142</p>
  </footer>
</main>

<!-- Right page: home -->
<main class="abs page-right">
  <div class="brand"><span class="dot"></span>COPPER FERN HERON</div>
  <nav class="nav"><span>Home</span><span>Service</span><span>Clients</span><span>Testimonials</span><span>About Us</span><span>News</span></nav>
  <div class="photo" role="img" aria-label="Hero photo: woman on a jetty between overwater villas and turquoise sea" style="left:22px;top:67px;width:318px;height:122px;background:linear-gradient(180deg,#2c63c9 0%,#6aa3e6 45%,#f0f3f6 52%,#3fc1dc 62%,#23a9d0 100%)"></div>
  <p class="abs" style="left:170px;top:194px;font-size:6px;letter-spacing:1px;color:#8b8fb0">•<span style="color:#ccc">••</span></p>
  <div class="rule" style="left:174px;top:214px;width:15px"></div>
  <p class="abs" style="left:83px;top:221px;width:196px;text-align:center;font-size:9.4px;line-height:1.4">Copper Fern Heron is a boutique lifestyle PR and communications agency helping brands get their voices heard in the UK.</p>
  <div class="btn" style="left:151px;top:266px;width:53px;height:20px;font-size:5.8px">Get in touch</div>

  <h2 class="abs service-title" style="left:22px;top:394px;font-size:12px">Our Service</h2>
  <div class="rule" style="left:22px;top:411px;width:16px"></div>
  <p class="abs" style="left:22px;top:416px;font-size:8.6px">Pure &amp; Simple</p>
  <p class="abs" style="left:22px;top:436px;width:140px;font-size:8.6px;line-height:1.5">No-nonsense approach to launching new brands to the UK market, offering a completely bespoke service to include</p>
  <div class="photo" role="img" aria-label="Photograph of a white resort hotel above a blue pool" style="left:212px;top:340px;width:131px;height:159px;border-radius:65px 65px 0 0;background:linear-gradient(180deg,#7fb3e4 0%,#cfe0ea 40%,#c9c1b3 62%,#3b7fbf 100%)"></div>
  <div class="services-band" style="left:0;top:499px;width:294px;height:78px;padding-left:22px;gap:16px">
    <div class="service-item" style="font-size:5px"><svg class="icon"><use href="#i-plan"/></svg>Strategic<br>Planning</div>
    <div class="service-item" style="font-size:5px"><svg class="icon"><use href="#i-media"/></svg>Consumer<br>Media Relations</div>
    <div class="service-item" style="font-size:5px"><svg class="icon"><use href="#i-rep"/></svg>Reputation<br>Management</div>
    <div class="service-item" style="font-size:5px"><svg class="icon"><use href="#i-star"/></svg>Influencer<br>Management</div>
    <div class="service-item" style="font-size:5px"><svg class="icon"><use href="#i-idea"/></svg>Creative<br>Consultation</div>
  </div>

  <h2 class="section-heading" style="top:625px;font-size:11.5px">Clients</h2>
  <div class="rule" style="left:173px;top:643px;width:15px"></div>
  <p class="abs" style="left:80px;top:650px;width:200px;text-align:center;font-size:8.6px;line-height:1.5">A dynamic collection of innovative lifestyle clients that we are wholly passionate about</p>
  <div class="photo" role="img" aria-label="Client photo: Selvane &amp; Co" style="left:48px;top:692px;width:82px;height:58px;background:#5b4a3e"><span style="position:absolute;left:27px;top:46px;font-size:3.8px;color:#fff">Selvane &amp; Co</span></div>
  <div class="photo" role="img" aria-label="Client photo: restaurant terrace" style="left:140px;top:692px;width:82px;height:58px;background:linear-gradient(180deg,#c97a5a,#6b3b2c)"></div>
  <div class="photo" role="img" aria-label="Client photo: framed portrait" style="left:232px;top:692px;width:82px;height:58px;background:radial-gradient(circle,#8a7040 30%,#eae6e1 60%)"></div>
  <div class="photo" role="img" aria-label="Client photo: dinner table setting" style="left:48px;top:756px;width:82px;height:58px;background:linear-gradient(135deg,#4d5a6e,#c4c8cf)"></div>
  <div class="photo" role="img" aria-label="Client photo: car on a beach" style="left:140px;top:756px;width:82px;height:58px;background:linear-gradient(180deg,#3b74c4 55%,#d9bd86 55%)"></div>
  <div class="photo" role="img" aria-label="Client photo: pour-over coffee" style="left:232px;top:756px;width:82px;height:58px;background:linear-gradient(90deg,#6e5444,#e9e3dc,#6e5444)"></div>
</main>

</body>
</html>
```